I need a book cover for a professional training book. I specialize in teaching financial professionals and insurance agents how to prospect and schedule first appointments by phone. My professional nickname is The DialMentor. I have been doing this training for over 30 years and am known to the industry. This book addresses the challenges the smartphone has created for the financial industry, which is a high trust profession. People are digitalizing every interaction but cannot do that with their financial advisor, so prospecting new clients has to adapt to the new world. I also address the changes the pandemic has added to this very old industry.
Please include my legal name : Merle T. Ashworth, and my nickname, The DialMentor (no spaces) on the cover
Updates

Title of my book is Booking Meetings in the Pocket Device Era. It is about how to prospect and set appointments by phone. My full name is Merle T. Ashworth and I want my branded (nickname) The DialMentor underneath it on the cover. If you want to use my logo, you can lift it from my website: www.dialmentor-example.com. My book is a training book for financial advisors, mostly newer ones. I have a built in market for a few reasons: 1. I have been training financial professionals for 30+ years. 2. I am well known in the industry. 3. Clients who hire me will buy 20 or more books at a time for their rookies. 4. I am promoting myself on WorkNexus and several professional friends tell others to buy my book. The book will not be on bookshelves in airports. It is not a novel. The industry I work in is more serious than silly. I already have a published book Current Calendar Building, Lead Finding and Calling for Money Managers. You can see it on Bookvale. I'd like to use a SIMILAR font on this book (or the same one). I do not want a purple book cover since it will create confusion between the two books. My audience runs from 22 year-olds fresh out of college to people over 60. It is not for one generation but all. I teach men, women, and all ethnicities, so I am concerned about a photo of someone holding a smartphone with obviously male/female hands. A good image will tell the story of getting appointments by phone without knowing the title. I will respond to your designs and messages quickly as I hope to make a decision soon. The book is already written and my editor is awaiting the artwork from you. Thank you in advance for accepting my project. Merle

Target Market(s)

Financial Advisors and Insurance Agents, Trainers and Manager in the financial services industry

Industry/Entity Type

Financial services, insurance

Requirements
Must have
• Clarity in the design
Should not have
• Illistrations or anything childish. This is a serious business but I don't want the cover to be boring and dour.

```html
<!DOCTYPE html>
<html lang="en">
<head>
<meta charset="utf-8">
<title>Booking Meetings in the Pocket Device Era — Book Cover</title>
<link rel="stylesheet" href="https://fonts.googleapis.com/css2?family=Montserrat:wght@800&family=Open+Sans:wght@400;600&display=swap">
<style>
  :root {
    --paper: #f1f1f1;
    --paper-light: #fafafa;
    --blue-deep: #0838e6;
    --blue-mid: #0a6cf2;
    --cyan-glow: #18d2ff;
    --author-blue: #0a3fe0;
    --shadow: #00134a;
  }
  html, body {
    margin: 0;
    padding: 0;
    width: 840px;
    height: 1200px;
    overflow: hidden;
    background: var(--paper);
  }
  .cover {
    position: relative;
    width: 840px;
    height: 1200px;
    overflow: hidden;
  }
  .cover-art {
    display: block;
    width: 840px;
    height: 1200px;
  }
  .title-line {
    font-family: "Montserrat", "Arial Black", sans-serif;
    font-weight: 800;
  }
  .author-name {
    font-family: "Open Sans", Arial, sans-serif;
    font-weight: 600;
    fill: var(--author-blue);
  }
  .author-brand {
    font-family: "Open Sans", Arial, sans-serif;
    font-weight: 400;
    fill: var(--author-blue);
  }
</style>
</head>
<body>
<main class="cover">
  <svg class="cover-art" viewBox="0 0 840 1200" xmlns="http://www.w3.org/2000/svg" aria-labelledby="cover-title">
    <title id="cover-title">Booking Meetings in the Pocket Device Era by Merle T. Ashworth, The DialMentor</title>
    <defs>
      <linearGradient id="paper-fill" x1="0" y1="0" x2="1" y2="1">
        <stop offset="0" stop-color="var(--paper-light)"/>
        <stop offset="1" stop-color="var(--paper)"/>
      </linearGradient>
      <radialGradient id="title-fill" cx="420" cy="330" r="420" gradientUnits="userSpaceOnUse">
        <stop offset="0" stop-color="var(--cyan-glow)"/>
        <stop offset="0.55" stop-color="var(--blue-mid)"/>
        <stop offset="1" stop-color="var(--blue-deep)"/>
      </radialGradient>
      <radialGradient id="band-fill" cx="420" cy="640" r="400" gradientUnits="userSpaceOnUse">
        <stop offset="0" stop-color="var(--cyan-glow)"/>
        <stop offset="0.5" stop-color="var(--blue-mid)"/>
        <stop offset="1" stop-color="var(--blue-deep)"/>
      </radialGradient>
      <filter id="sheet-shadow" x="-5%" y="-10%" width="110%" height="130%">
        <feDropShadow dx="0" dy="2" stdDeviation="5" flood-color="var(--shadow)" flood-opacity="0.35"/>
      </filter>
    </defs>

    <!-- blue band -->
    <rect class="reveal-band" x="0" y="600" width="840" height="430" fill="url(#band-fill)"/>

    <!-- lower paper sheet -->
    <rect class="paper-lower" x="-10" y="1002" width="860" height="210" fill="url(#paper-fill)" filter="url(#sheet-shadow)"/>

    <!-- upper paper sheet -->
    <rect class="paper-upper" x="-10" y="-10" width="860" height="642" fill="url(#paper-fill)" filter="url(#sheet-shadow)"/>

    <!-- title, upper block -->
    <g class="title-upper" fill="url(#title-fill)">
      <text class="title-line" x="60" y="296" font-size="205" textLength="716" lengthAdjust="spacingAndGlyphs">BOOKING</text>
      <text class="title-line" x="58" y="412" font-size="110" textLength="722" lengthAdjust="spacingAndGlyphs">MEETINGS</text>
      <text class="title-line" x="188" y="568" font-size="172" textLength="464" lengthAdjust="spacingAndGlyphs">IN THE</text>
    </g>

    <!-- title, band block -->
    <g class="title-band" fill="var(--paper)">
      <text class="title-line" x="46" y="752" font-size="126" textLength="742" lengthAdjust="spacingAndGlyphs">POCKET DEVICE</text>
      <text class="title-line" x="100" y="960" font-size="232" textLength="640" lengthAdjust="spacingAndGlyphs">ERA</text>
    </g>

    <!-- author -->
    <text class="author-name" x="420" y="1104" font-size="44" text-anchor="middle" textLength="520" lengthAdjust="spacing">MERLE T. ASHWORTH</text>
    <text class="author-brand" x="420" y="1162" font-size="32" text-anchor="middle">The DialMentor</text>
  </svg>
</main>
</body>
</html>
```